Meadowlark Lane Yoga Facebook Design

"Practice Radiant Movement"

Foundational and sustainable yoga practice to cultivate growth through a variety of anatomy- informed movement patterns. Develop an informative and inspirational connection with the mind, body and spirit, through smart and integrated movement.

-I need a design that is happy and cheerful and attracts children and adults alike. I teach vinyassa based yoga that is sustainable and smart, kid yoga, and chair yoga.

-A movement practic rooted in foundation, core, and expression

- Accessible yoga for a sustained practice. A guided movement practice where one gains information and knowledge of oneself through a mind/body connection. For one feel good physically with a new awareness of their internal radiance that exists in all beings. Physical rejuvenation egnites a light and increases energy to flow through the physical body, which ultimately tranlates into works of kindness for others and out in the world.

Nora Whitfield
Yoga Instructor
MD, Pediatrician
RYT-200
RCYT
Certified yoga teacher for adults and children

Full description:
What is the positioning or mission statement of your company? to guide individuals in a yoga-based safe and sustainable movement practice applicable to all ages and body types. Currently my focus is working with children in daycare and school settings, but my goal is to expand into private yoga practice for adults, and potentially as part of rented space in studios. I hope to find a way to work with children AND adults (so would love for logo to be appealing to both), but current focus is with children based on need and demand in the community. yoga for children also compliments my backround as a pediatrician/neonatologist, and I greatly miss interacting with children. I also want to emphasize a yoga/movement practice that is focused more on what one feels internally through movement. NOT what one looks like asthetically. I believe in removing all mirrors from yoga/movement practice. It should be an experience of movement/poses/yoga through appropriate cueing and education. It is not about the details of how far the knee should bend, or how high the leg should be. Focusing on foudation first, core, then core engagement and ultimately expression of poses/movements. A focus on strength, stability and mobility, not just flexibility, which is the common perception/association with yoga. I also want individuals to learn to be an advocate of their own health. Through guidance, I hope for individuals to connect with their body so they know themselves so well to be able to advocate for themselves in the modern healthcare world. This internal experience and connection is so essential in a world where modern medicine has become a business and it is all about making a dollar. the connection with patients is lost, and individuals need to learn to empower themselves and through their new found voice to be able to articulate what is wrong.
Does your company have a tagline or slogan that should be included with the logo? "Practice Radiant Movement"
What do you hope your company can be known for? Accessible yoga for a sustained practice. A guided movement practice where one gains information and knowledge of oneself through a mind/body connection. For one feel good physically with a new awareness of their internal radiance that exists in all beings. Physical rejuvenation egnites a light and increases energy to flow through the physical body, which ultimately tranlates into works of kindness for others and out in the world.
What color palettes might you prefer? why? love the colors currently chosen
Where will the logo be primarily used? initially business cards, but hopefully future websites, t-shirts, and potentially local magazine adds. Also starting with a small couple of banners for community events in the area. I currently practice as a nomad out of my car :)
Are there any elements you would prefer to see in the logo? Movement. A modern depiction of a human body/figure practicing movement. Hoping to avoid a stereotypical yoga pose per say, just because I want to people to think of it more of a movement practice with yoga roots. Modern yoga. There are elements of breathing and connecting with oneself through the flow of breath and movement, but I do not focus on the meditative/cerebral aspect of the yoga practice. What I teach is almost reaching a meditative state through movement. I personally don't practice, nor resonate with just seated meditation. just not my thing :)
In your opinion, what defines a well-designed logo? curiosity. enough info for individuals to think they know what it means, but want to know more. invokes curiosity, but not too abstract. Reproducible. not too complicated. I want also to invoke a community feel, so a design that appeals to all people within a community.
What is your preference in reference to icons, typography, spokespeople (characters), etc.? modern design. I love the idea of a logo for my purposes, to invoke a sense of movement from within. So not too static.
What words or icons must be included in the logo? movement with yoga roots.
What logos do you like and why? A representation, but not exact. I think some ambiguity is intriguing for others, and also memorable. I want it to be an artistic representation of movement/yoga
What logos do you dislike and why? too busy, too loud.
In your opinion, what is the primary purpose for a logo? association
Who is the primary target audience? (who is most likely to use your services/product?) Children and their parents, but ultimately to expand into teaching adults. I even have aspirations of prenatal and post-natal yoga. Potentially incorporating infants.
Who currently uses your product the most? n/a (working in schools/daycare currently. It is currently all volunteer)
Are you pleased with the range of people your company serves? n/a
Are you looking to expand, modify, or completely change your target audience? or will it remain the same? yes! expand into an adult audience.
How do you plan to focus on your target audience? currently by working through schools and daycares. hopefully ultimately through after school care programs and then offering kid yoga in an existing yoga studio (working on this with Q studio in Ridgeland, currently)
What are your main forms of advertising? word of mouth, schools, daycares. Happy kids talking to their parents about the yoga class they took and happy teachers :)
How do most customers find out about your company?
Which gender are you targeting? All genders! However, with kid yoga, often the maternal individual in the child's life is more involved with decision making as far as extracurricular activities

Target Market(s)

Adults, children and families interested in movement, wellness and fun

Font styles to use
Sans Serif

Requirements
Must have
• ***I meant to emphasize the that "S" figure in my logo is SOOO iimportant to me. My daughter designed it. please highlight the "S" figure if possible******
My logo and the phrase "practice radiant movement"
Same colors as my logo
Feel like movement and fun.
Attracts children and families
Incorporate pieces of my description somehow
Nice to have
• different yoga poses or figures in movement
abstract design
attacts all body types and genders
inclusive

Industry is yoga, movement, wellness
Should not have
• no darkness
want happy and vibrant, inviting

```html
<!DOCTYPE html>
<html lang="en">
<head>
<meta charset="utf-8">
<title>Meadowlark Lane Yoga – Cover Banner</title>
<link href="https://fonts.googleapis.com/css2?family=Baloo+2:wght@400;500;700&display=swap" rel="stylesheet">
<style>
  :root {
    --page-bg: #f8f6e4;
    --cream-light: #fffdf4;
    --cream-edge: #f4eed4;
    --teal: #3f9ea6;
    --teal-soft: #62c2c4;
    --lime: #a9cf72;
    --sun-yellow: #f3d63b;
    --ink-grey: #5a5a58;
    --white: #ffffff;
  }
  * { margin: 0; padding: 0; box-sizing: border-box; }
  html, body {
    width: 1180px;
    height: 1200px;
    overflow: hidden;
    background: var(--page-bg);
  }
  .stage {
    position: relative;
    width: 1180px;
    height: 1200px;
  }
  .cover-banner {
    position: absolute;
    left: 40px;
    top: 390px;
    width: 1100px;
    height: 419px;
    box-shadow: 0 30px 60px rgba(150, 140, 90, 0.25);
    border: 1px solid #e4dfc4;
  }
  .cover-banner svg { display: block; width: 100%; height: 100%; }
  .tagline-small {
    font-family: "Baloo 2", sans-serif;
    font-weight: 400;
    font-size: 25px;
    fill: var(--ink-grey);
    letter-spacing: 0.5px;
  }
  .tagline-large {
    font-family: "Baloo 2", sans-serif;
    font-weight: 700;
    font-size: 78px;
    fill: var(--teal);
  }
  .badge-name {
    font-family: "Baloo 2", sans-serif;
    font-weight: 500;
    font-size: 10px;
    fill: var(--teal);
  }
</style>
</head>
<body>
<main class="stage">
  <section class="cover-banner" aria-label="Meadowlark Lane Yoga cover banner">
    <svg viewBox="0 0 930 354" xmlns="http://www.w3.org/2000/svg">
      <defs>
        <radialGradient id="creamGlow" cx="0.5" cy="0.45" r="0.6">
          <stop offset="0" stop-color="var(--cream-light)"/>
          <stop offset="1" stop-color="var(--cream-edge)"/>
        </radialGradient>
        <linearGradient id="seaPhotoTones" x1="0" y1="0" x2="0" y2="1">
          <stop offset="0" stop-color="#e9d2b0"/>
          <stop offset="0.45" stop-color="#9fb4b0"/>
          <stop offset="1" stop-color="#5f8a92"/>
        </linearGradient>
        <linearGradient id="gardenPhotoTones" x1="0" y1="0" x2="0" y2="1">
          <stop offset="0" stop-color="#7e9a58"/>
          <stop offset="0.5" stop-color="#8c86b8"/>
          <stop offset="1" stop-color="#6f9a3e"/>
        </linearGradient>
        <linearGradient id="edgeStroke" x1="0" y1="0" x2="0" y2="1">
          <stop offset="0" stop-color="var(--teal-soft)"/>
          <stop offset="0.5" stop-color="var(--lime)"/>
          <stop offset="1" stop-color="var(--sun-yellow)"/>
        </linearGradient>
        <linearGradient id="edgeStrokeRight" x1="0" y1="0" x2="0" y2="1">
          <stop offset="0" stop-color="var(--sun-yellow)"/>
          <stop offset="0.5" stop-color="var(--lime)"/>
          <stop offset="1" stop-color="var(--teal-soft)"/>
        </linearGradient>
        <linearGradient id="dotFill" x1="0" y1="0" x2="0" y2="1">
          <stop offset="0" stop-color="var(--sun-yellow)"/>
          <stop offset="1" stop-color="var(--teal-soft)"/>
        </linearGradient>
        <radialGradient id="spiralHaze" cx="0.5" cy="0.5" r="0.5">
          <stop offset="0" stop-color="var(--sun-yellow)" stop-opacity="0.45"/>
          <stop offset="1" stop-color="var(--sun-yellow)" stop-opacity="0"/>
        </radialGradient>
      </defs>

      <rect class="cover-base" width="930" height="354" fill="url(#creamGlow)"/>

      <!-- soft spiral areas -->
      <circle role="img" aria-label="Yellow hand-drawn spiral" cx="585" cy="22" r="60" fill="url(#spiralHaze)"/>
      <circle role="img" aria-label="Yellow hand-drawn spiral" cx="325" cy="322" r="80" fill="url(#spiralHaze)"/>

      <!-- left photo panel -->
      <path role="img" aria-label="Photo of a person doing a raised-arm yoga pose by the sea and cliffs"
            d="M0 0 H270 C300 60 200 120 140 170 C110 205 175 270 155 354 H0 Z"
            fill="url(#seaPhotoTones)"/>
      <path class="panel-edge" d="M270 0 C300 60 200 120 140 170 C110 205 175 270 155 354"
            fill="none" stroke="url(#edgeStroke)" stroke-width="8"/>

      <!-- right photo panel -->
      <path role="img" aria-label="Photo of a child meditating cross-legged on grass in a garden"
            d="M930 0 H748 C730 20 770 90 745 140 C720 190 620 200 575 290 C565 315 568 335 568 354 H930 Z"
            fill="url(#gardenPhotoTones)"/>
      <path class="panel-edge" d="M748 0 C730 20 770 90 745 140 C720 190 620 200 575 290 C565 315 568 335 568 354"
            fill="none" stroke="url(#edgeStrokeRight)" stroke-width="8"/>

      <!-- accent dots -->
      <circle class="accent-dot" cx="209" cy="196" r="30" fill="url(#dotFill)"/>
      <circle class="accent-dot" cx="719" cy="134" r="15" fill="url(#dotFill)"/>
      <circle class="accent-dot" cx="500" cy="354" r="23" fill="url(#dotFill)"/>

      <!-- tagline -->
      <text class="tagline-small" x="290" y="100">practice radiant</text>
      <text class="tagline-large" x="288" y="156">movement</text>

      <!-- brand badge -->
      <g class="brand-badge">
        <circle cx="794" cy="326" r="44" fill="var(--white)"/>
        <text class="badge-name" x="794" y="320" text-anchor="middle">Meadowlark</text>
        <text class="badge-name" x="794" y="332" text-anchor="middle">Lane Yoga</text>
      </g>
    </svg>
  </section>
</main>
</body>
</html>
```